Bref créative
business card and letter head
TCW Roofing & Decks, LLC
Corporate
Dale Harrington
Project Manager / Estimator
7426-B Ferncliff
Houston, TX 77094
daleh4182@quorvix.com
Logo for TCW Roofing & Decks, LLC

```html
<!DOCTYPE html>
<html lang="en">
<head>
<meta charset="utf-8">
<title>TCW Roofing &amp; Decks, LLC — Business Card</title>
<link rel="stylesheet" href="https://fonts.googleapis.com/css2?family=Roboto+Condensed:wght@400;700;900&display=swap">
<style>
  :root {
    --navy: #173a6b;
    --navy-deep: #0f2b54;
    --sky: #6f95c4;
    --paper: #ffffff;
    --ink: #2a3d5c;
    --stage: #eceef1;
  }
  * { box-sizing: border-box; margin: 0; padding: 0; }
  html, body { width: 1200px; height: 980px; overflow: hidden; background: var(--stage); }
  body { position: relative; font-family: "Roboto Condensed", Arial, sans-serif; }

  .card {
    position: absolute;
    width: 560px;
    height: 320px;
    border-radius: 22px;
    overflow: hidden;
    box-shadow: 0 10px 28px rgba(20, 35, 60, 0.18);
  }

  /* back side */
  .card-back {
    left: 580px; top: 110px;
    background: var(--navy);
    display: flex; flex-direction: column; align-items: center; justify-content: center;
  }
  .card-back .brand-mark {
    color: var(--paper);
    font-weight: 900;
    font-size: 104px;
    letter-spacing: 2px;
    line-height: 1;
  }
  .card-back .web {
    margin-top: 22px;
    color: #c9d6ea;
    font-size: 13px;
    letter-spacing: 4px;
    text-transform: uppercase;
  }

  /* front side */
  .card-front {
    left: 60px; top: 540px;
    background: var(--paper);
  }
  .swoosh { position: absolute; inset: 0; width: 100%; height: 100%; }

  .contact {
    position: absolute; left: 30px; top: 22px;
    list-style: none;
    color: var(--ink);
    font-size: 12px;
    letter-spacing: 1.4px;
    text-transform: uppercase;
  }
  .contact li { display: flex; align-items: center; height: 17px; }
  .contact .email, .contact .web-line { text-transform: none; letter-spacing: 1px; }
  .contact .dot {
    width: 10px; height: 10px; border-radius: 50%;
    background: var(--navy); margin-right: 9px; flex: none;
  }
  .contact .spacer { width: 10px; margin-right: 9px; flex: none; }

  .logo {
    position: absolute; left: 262px; top: 40px;
    color: var(--navy);
    font-weight: 900;
    text-align: left;
  }
  .logo .initials { display: block; font-size: 96px; line-height: 0.9; letter-spacing: 2px; }
  .logo .company { display: block; font-size: 27px; line-height: 1.1; }

  .person {
    position: absolute; right: 28px; bottom: 18px;
    text-align: right; color: var(--paper);
    text-transform: uppercase;
  }
  .person .name { font-size: 16px; letter-spacing: 2px; font-weight: 700; }
  .person .title { font-size: 12px; letter-spacing: 2px; margin-top: 3px; }
</style>
</head>
<body>

  <section class="card card-back" aria-label="Card back">
    <div class="brand-mark">TCW</div>
    <div class="web">www.tcwroofdecks.com</div>
  </section>

  <section class="card card-front" aria-label="Card front">
    <svg class="swoosh" viewBox="0 0 560 320" preserveAspectRatio="none" aria-hidden="true">
      <path d="M0 182 C150 234 350 250 560 238" fill="none" stroke="var(--sky)" stroke-width="2"/>
      <path d="M0 198 C150 246 350 262 560 250 L560 320 L0 320 Z" fill="var(--navy)"/>
      <path d="M0 222 C170 264 360 270 560 258" fill="none" stroke="var(--sky)" stroke-width="1.5" opacity="0.6"/>
    </svg>

    <ul class="contact">
      <li><span class="dot"></span>7426-B Ferncliff</li>
      <li><span class="spacer"></span>Houston, TX 77094</li>
      <li><span class="dot"></span>713-555-0148</li>
      <li><span class="dot"></span>832-555-0192</li>
      <li><span class="dot"></span>dale4182</li>
      <li class="email"><span class="dot"></span>daleh4182@quorvix.com</li>
      <li class="web-line"><span class="dot"></span>www.tcwroofdecks.com</li>
      <li><span class="dot"></span>832-555-0176</li>
    </ul>

    <div class="logo">
      <span class="initials">TCW</span>
      <span class="company">Roofing &amp; Decks, LLC</span>
    </div>

    <div class="person">
      <div class="name">Dale Harrington</div>
      <div class="title">Project Manager / Estimator</div>
    </div>
  </section>

</body>
</html>
```